Premium Honey Fusions need a label design. 5 awesome blends (see below)

We need a label design for a line of honey. Brand is an existing brand called MELVORIN. www.melvorinusa.example
MELVORIN is a line of juices. The honey line is an extension of the MELVORIN juice line.
Blends are:
Honey Cinnamon
Honey Saffron
Honey Ginger
Honey Herbs
Honey Wild Flower
PRODUCT FROM INDIA
We need a label design for a line of honey. Brand is an existing brand called MELVORIN.
See www.melvorinusa.example
We would like to see label designs that:
-are easy to read, clean
-"Honey Cinnamon”, etc... should be prominent, as it will be what will set us apart.
-use colors that communicate "premium honey"
-premium
-unique
-healthy/good for you
-We need a “Help us save the bees” type message on the logo. We will give % of profit from sale of honey to go towards saving the bees.
The final design should communicate :
-healthy
-DELICIOUS!!!! (it is!)
-premium
-unique
-exotic
Glass bottle is square (see pics) and label has 3 sides:
Front panel
Side panel 1: will be nutritional, ingredients, UPC, etc
Side panel 2: a story about bees? about saffron, about cinnamon??
Target Market(s)
Hispanic and American markets.
Healthy conscious people.
Premium honey market
Look and feel

```html
<!DOCTYPE html>
<html lang="en">
<head>
<meta charset="utf-8">
<title>MELVORIN Premium Honey Cinnamon Label</title>
<link rel="stylesheet" href="https://fonts.googleapis.com/css2?family=Merriweather:wght@900&family=Montserrat:wght@500;700&family=Kaushan+Script&family=Lora:wght@700&display=swap">
<style>
  :root {
    --navy: #1f2940;
    --gold: #b99a4e;
    --khaki: #c8bd8c;
    --cream: #f3efe2;
    --white: #ffffff;
    --logo-red: #d3262b;
  }
  html, body {
    margin: 0;
    padding: 0;
    width: 1200px;
    height: 1080px;
    overflow: hidden;
    background: var(--white);
  }
  .canvas {
    position: relative;
    width: 1200px;
    height: 1080px;
  }
  .label {
    position: absolute;
    left: 230px;
    top: 200px;
    width: 660px;
    height: 680px;
  }
  .label-shapes {
    position: absolute;
    inset: 0;
  }
  .label-text {
    position: absolute;
    left: 62px;
    width: 536px;
    text-align: center;
    margin: 0;
  }
  .brand-name {
    top: 74px;
    font-family: "Montserrat", sans-serif;
    font-weight: 700;
    font-size: 26px;
    letter-spacing: 1px;
    color: var(--logo-red);
  }
  .tier {
    top: 182px;
    font-family: "Montserrat", sans-serif;
    font-weight: 500;
    font-size: 26px;
    letter-spacing: 3px;
    color: var(--khaki);
  }
  .claim {
    top: 238px;
    font-family: "Kaushan Script", cursive;
    font-size: 40px;
    color: var(--white);
  }
  .flavour {
    top: 300px;
    font-family: "Merriweather", serif;
    font-weight: 900;
    font-size: 62px;
    line-height: 66px;
    color: var(--gold);
  }
  .bee-mark {
    position: absolute;
    left: 305px;
    top: 468px;
    width: 50px;
    height: 42px;
    border-radius: 50%;
    background: radial-gradient(circle at 45% 60%, #f0d94a 0 30%, var(--navy) 32% 100%);
    border: 2px solid var(--cream);
    box-sizing: border-box;
  }
  .cause {
    top: 528px;
    font-family: "Kaushan Script", cursive;
    font-size: 14px;
    color: var(--white);
  }
  .origin {
    top: 568px;
    font-family: "Lora", serif;
    font-weight: 700;
    font-size: 21px;
    color: var(--white);
  }
  .weight {
    position: absolute;
    left: 92px;
    top: 568px;
    margin: 0;
    font-family: "Lora", serif;
    font-weight: 700;
    font-size: 21px;
    color: var(--white);
  }
  .palette {
    position: absolute;
    left: 1010px;
    top: 600px;
    display: flex;
    flex-direction: column;
    gap: 12px;
  }
  .swatch {
    width: 62px;
    height: 62px;
  }
  .swatch-navy { background: var(--navy); }
  .swatch-gold { background: var(--gold); }
  .swatch-khaki { background: var(--khaki); }
</style>
</head>
<body>
<main class="canvas">
  <section class="label">
    <svg class="label-shapes" viewBox="0 0 660 680" width="660" height="680" aria-hidden="true">
      <rect class="wrap-band" x="0" y="180" width="660" height="390" fill="var(--navy)"/>
      <g class="band-rules" stroke="var(--khaki)" stroke-width="2" fill="none">
        <line x1="0" y1="192" x2="660" y2="192"/>
        <line x1="0" y1="200" x2="660" y2="200"/>
        <line x1="0" y1="550" x2="660" y2="550"/>
        <line x1="0" y1="558" x2="660" y2="558"/>
        <line x1="34" y1="240" x2="34" y2="510"/>
        <line x1="626" y1="240" x2="626" y2="510"/>
      </g>
      <path class="front-arch" d="M62,660 V268 A268,268 0 0 1 598,268 V660 Z" fill="var(--navy)"/>
      <path class="arch-rule-outer" d="M76,646 V268 A254,254 0 0 1 584,268 V646 Z" fill="none" stroke="var(--khaki)" stroke-width="3"/>
      <path class="arch-rule-inner" d="M86,636 V268 A244,244 0 0 1 574,268 V636 Z" fill="none" stroke="var(--gold)" stroke-width="1.5"/>
      <g class="tier-rules" stroke="var(--khaki)" stroke-width="1">
        <line x1="172" y1="198" x2="232" y2="198"/>
        <line x1="428" y1="198" x2="488" y2="198"/>
      </g>
      <line class="flavour-rule" x1="148" y1="450" x2="512" y2="450" stroke="var(--cream)" stroke-width="1.5"/>
    </svg>

    <p class="label-text brand-name">MELVORIN</p>
    <p class="label-text tier">PREMIUM</p>
    <p class="label-text claim">All Natural</p>
    <h1 class="label-text flavour">Honey<br>Cinnamon</h1>
    <div class="bee-mark" role="img" aria-label="Small line drawing of a bee"></div>
    <p class="label-text cause">Part of the profit goes to bees conservation efforts</p>
    <p class="weight">18 oz</p>
    <p class="label-text origin">Product of India</p>
  </section>

  <aside class="palette" aria-label="Colour palette">
    <div class="swatch swatch-navy"></div>
    <div class="swatch swatch-gold"></div>
    <div class="swatch swatch-khaki"></div>
  </aside>
</main>
</body>
</html>
```